Walter Hobbs PA Card Logo

Current logo attached. Its 25 year old logo I have used. Looking for a new fresh elegant professional look/design for a law firm that has high net worth clientele and is estate planning business law firm. Firm mis in Palm Beach Florida.
One sided card linen stock white will be used. Logo section name section. Logo should include nice elegant design using the letter "G" perhapa (I am not wed to current font of the G on current logo.) Be creative there with logo design. My initials are WH.......color scheme I figure 3 tone... Raised Gold Foil, Blue name of firm = Walter Hobbs, P.A. My practice focus is Family and Business Asset Protection. My name is Walter W. Hobbs, Esq. Practice specialties include Asset Protection trusts, Business Succession Planning, LLC law, Estate Planning, Medicaid Planning (Maybe put those topics in bullets in a section of card. Bottom of card can be reserved smaller print address phone website and email address. Address section is not as important as logo and topics of practice on front. I foresee address section can be in dark blue. MY name and Topics dark blue as well.
Target Market(s)
affluent; business owners executives; wealth 2-10 million net worth
Industry/Entity Type
business law and estate planning
Contact Information for Business Card
White thick linen one sided

```html
<!DOCTYPE html>
<html lang="en">
<head>
<meta charset="utf-8">
<title>Walter Hobbs, P.A. — Business Card</title>
<link rel="stylesheet" href="https://fonts.googleapis.com/css2?family=Kaushan+Script&family=Tinos:wght@400&display=swap">
<style>
  :root {
    --navy: #16406e;
    --gold: #dba72b;
    --card: #fbfbfa;
    --stage: #e7e4df;
  }
  * { margin: 0; padding: 0; box-sizing: border-box; }
  html, body {
    width: 1200px; height: 780px; overflow: hidden;
    background: var(--stage);
  }
  .card {
    position: absolute; left: 120px; top: 115px;
    width: 960px; height: 549px;
    background: var(--card);
    box-shadow: 0 10px 30px rgba(0,0,0,.18);
    font-family: "Tinos", "Times New Roman", serif;
    color: var(--navy);
  }
  .firm {
    position: absolute; left: 150px; top: 120px;
    display: flex; flex-direction: column; align-items: flex-start;
  }
  .firm-row { display: flex; align-items: center; gap: 18px; }
  .firm-mark {
    width: 26px; height: 26px; background: var(--gold);
  }
  .firm-name {
    font-size: 58px; line-height: 1; color: var(--navy);
  }
  .firm-tagline {
    margin-top: 14px; margin-left: 44px;
    font-size: 14px; letter-spacing: 10px; color: var(--navy);
  }
  .person {
    position: absolute; left: 520px; top: 300px;
    font-family: "Kaushan Script", cursive;
    font-size: 44px; color: var(--navy);
  }
  .divider {
    position: absolute; left: 110px; right: 40px; top: 388px;
    height: 2px; background: var(--gold);
  }
  .contact {
    position: absolute; left: 92px; top: 412px;
    display: flex; gap: 14px; align-items: flex-end;
  }
  .contact-icons { display: flex; flex-direction: column-reverse; gap: 8px; padding-bottom: 2px; }
  .contact-icons svg { width: 24px; height: 24px; display: block; }
  .contact-lines, .address-lines { font-size: 25px; line-height: 34px; }
  .address {
    position: absolute; left: 600px; top: 412px;
  }
  .web-domain { color: var(--gold); }
</style>
</head>
<body>
  <main class="card">
    <div class="firm">
      <div class="firm-row">
        <span class="firm-mark" aria-hidden="true"></span>
        <span class="firm-name">Walter Hobbs, P.A.</span>
      </div>
      <span class="firm-tagline">ELDER LAW ATTORNEY</span>
    </div>

    <p class="person">Daniel Reyes</p>

    <div class="divider" aria-hidden="true"></div>

    <section class="contact">
      <div class="contact-icons" aria-hidden="true">
        <svg viewBox="0 0 24 24"><circle cx="12" cy="12" r="12" fill="var(--gold)"/><rect x="6.5" y="8" width="11" height="8" fill="none" stroke="#fff" stroke-width="1.5"/><path d="M6.5 8 L12 12.5 L17.5 8" fill="none" stroke="#fff" stroke-width="1.5"/></svg>
        <svg viewBox="0 0 24 24"><circle cx="12" cy="12" r="12" fill="var(--gold)"/><rect x="6" y="10" width="12" height="7" rx="1" fill="none" stroke="#fff" stroke-width="1.5"/><rect x="8.5" y="6.5" width="7" height="3.5" fill="none" stroke="#fff" stroke-width="1.3"/></svg>
        <svg viewBox="0 0 24 24"><circle cx="12" cy="12" r="12" fill="var(--gold)"/><rect x="8" y="5.5" width="8" height="13" rx="1.5" fill="none" stroke="#fff" stroke-width="1.5"/><circle cx="12" cy="16" r="0.9" fill="#fff"/></svg>
      </div>
      <div class="contact-lines">
        <p>(01) 4821 3907</p>
        <p>(01) 4821 3908</p>
        <p>info@hobbslawmail.com</p>
      </div>
    </section>

    <section class="address">
      <div class="address-lines">
        <p>PO BOX 418 Ocean Avenue</p>
        <p>3rd street Palm Beach</p>
        <p>www.<span class="web-domain">hobbslawfirm</span>.com</p>
      </div>
    </section>
  </main>
</body>
</html>
```